Maple Crest Glow Skin Studio needs an 8 page WP redesign

We need a colorful re-design for an 8 page Wordpress website. The current preliminary website is live. The home page URL is http://maplecrestglowskinstudio.example The new logo is live on the website also. I would like a (re)design using the colors that are represented by the new logo file, and any additional complimentary colors. The information regarding the business can be found on the website already, so please review it for insight. The name of the business is "Maple Crest Glow Skin Studio".

Target Market(s)

The targeted website viewer is an adult female between the ages of 30 and 75 who is interested in facial renewal, wart removal and scar removal. This website should inspire in the target viewer the benefits of laser facial renewal, wart removal and new scar removal. Potential website viewers are wanting and searching for improved skin health and appearance. The website must represent the essence of a professional spa business.

Industry/Entity Type

Business

Font styles to use
Sans Serif

Requirements
Must have
• - The phone number placed in a visible and high value widget area that allows mobile phone browser dialing.

```html
<!DOCTYPE html>
<html lang="en">
<head>
<meta charset="utf-8">
<title>Maple Crest Glow Skin Studio</title>
<link href="https://fonts.googleapis.com/css2?family=Open+Sans:wght@300;400;600;700;800&family=Oswald:wght@500&display=swap" rel="stylesheet">
<style>
:root{
  --plum-dark:#3b1538;
  --plum:#5e2259;
  --magenta:#b42ab0;
  --magenta-bright:#e23fdc;
  --pink-glow:#f26cf0;
  --ink:#333;
  --muted:#666;
  --grey-bg:#e4e4e4;
  --night:#1b1b1b;
  --night-2:#262626;
  --white:#fff;
}
*{box-sizing:border-box;margin:0;padding:0}
html,body{width:1200px;height:2677px;overflow:hidden}
body{position:relative;font-family:"Open Sans",Arial,sans-serif;color:var(--ink);background:var(--white)}
.abs{position:absolute}

/* header */
.hero-photo{left:0;top:0;width:1200px;height:575px;background:linear-gradient(120deg,#cfd3d6 0%,#e9e5e0 35%,#c9b8a6 60%,#8f7a6a 100%)}
.hero-shade{left:0;top:380px;width:1200px;height:195px;background:linear-gradient(180deg,rgba(0,0,0,0),rgba(40,20,40,.45))}
.topbar{left:0;top:0;width:1200px;height:60px;background:rgba(70,25,66,.92)}
.nav{top:0;height:60px;display:flex;align-items:center;gap:24px;list-style:none}
.nav li{color:var(--white);font-size:12px;font-weight:700;text-transform:uppercase}
.nav-left{left:160px}
.nav-right{left:760px}
.brand{left:450px;top:8px;width:300px;height:110px;display:flex;align-items:center;justify-content:center;gap:10px}
.brand-dot{width:18px;height:18px;border-radius:50%;background:var(--magenta-bright)}
.brand-name{font-size:25px;font-weight:800;color:var(--white);line-height:1.1;text-align:center;width:240px}
.hero-title{left:0;width:1200px;top:468px;text-align:center;color:var(--white);font-size:40px;font-weight:700;letter-spacing:2px;text-transform:uppercase}
.call-pill{left:488px;top:545px;width:225px;height:62px;border-radius:31px;background:var(--plum-dark);color:var(--white);text-align:center;padding-top:9px;z-index:2}
.call-pill small{display:block;font-size:11px;font-weight:600}
.call-pill a{color:var(--white);text-decoration:none;font-size:21px;font-weight:700}

/* offer band */
.offers{left:0;top:575px;width:1200px;height:317px;background:var(--magenta)}
.offers h2{position:absolute;top:42px;width:1200px;text-align:center;color:var(--white);font-weight:400;font-size:29px}
.offers p{position:absolute;top:84px;width:1200px;text-align:center;color:var(--white);font-size:12px;line-height:16px}
.deal{position:absolute;top:140px;width:136px;height:136px;border-radius:50%;background:var(--magenta-bright);border:8px solid #c94fc6;box-shadow:0 6px 14px rgba(0,0,0,.25);color:var(--white);text-align:center;padding-top:26px}
.deal b{display:block;font-size:32px;font-weight:700;line-height:36px}
.deal span{display:block;font-size:10px;line-height:13px;text-transform:uppercase}
.deal-chev{position:absolute;top:150px}

/* intro */
.intro-copy{left:160px;top:942px;width:400px}
.intro-copy h2{font-size:29px;font-weight:300;line-height:32px;color:#444;margin-bottom:14px}
.intro-copy p{font-size:11px;line-height:17px;color:var(--muted);margin-bottom:12px}
.btn-more{display:inline-block;background:#ddd;color:#666;font-size:11px;padding:6px 12px;border-radius:2px;margin-top:2px}
.faq{left:611px;top:945px;width:429px}
.faq-item{display:flex;align-items:center;height:50px;background:var(--grey-bg);border-radius:0 25px 25px 0;margin-bottom:10px;font-size:12px;color:#444}
.faq-ico{width:52px;height:50px;background:var(--plum-dark);color:var(--white);font-size:24px;font-weight:700;display:flex;align-items:center;justify-content:center;margin-right:14px}
.faq-body{padding:4px 0 16px 52px;font-size:11px;line-height:17px;color:var(--muted)}
.faq-body p{margin-bottom:10px}

/* benefits */
.benefits{left:0;top:1320px;width:1200px;height:478px;background:radial-gradient(ellipse at 50% 40%,#333 0%,#151515 75%)}
.benefits h2{position:absolute;top:44px;width:1200px;text-align:center;color:var(--white);font-weight:300;font-size:29px}
.benefits .lead{position:absolute;top:86px;width:1200px;text-align:center;color:var(--white);font-size:11px;font-weight:600}
.card{position:absolute;top:118px;width:280px;height:302px;background:#ececec;border-radius:4px;padding:16px}
.card-img{height:136px;border:4px solid var(--white)}
.card h3{color:var(--magenta);font-size:15px;font-weight:700;text-transform:uppercase;line-height:18px;margin:26px 0 8px}
.card p{font-size:11px;line-height:17px;color:var(--muted)}
.card-plus{position:absolute;left:124px;bottom:-14px;width:30px;height:30px;border-radius:50%;background:#ececec;text-align:center;font-size:16px;line-height:28px;color:var(--magenta)}

/* videos */
.videos-head{left:160px;top:1842px;width:580px}
.videos-head h2{font-size:29px;font-weight:300;color:#444;margin-bottom:10px}
.videos-head p{font-size:11px;line-height:17px;color:var(--muted)}
.video{left:160px;top:1975px;width:578px;height:358px;background:linear-gradient(135deg,#2f3b3e,#54656a 50%,#2a3336)}
.video-btn{left:373px;top:2133px;width:150px;height:44px;background:var(--magenta);color:var(--white);font-size:12px;display:flex;align-items:center;justify-content:center;gap:10px}
.consult{left:770px;top:1900px;width:270px;height:433px;background:#f0f0f0;border-radius:12px;border:1px solid #ddd;padding:8px}
.consult h3{height:48px;border-radius:10px 10px 0 0;background:var(--magenta);color:var(--white);font-family:"Oswald",Arial,sans-serif;font-weight:500;font-size:20px;text-align:center;line-height:48px;text-transform:uppercase}
.field{height:34px;background:var(--white);border:1px solid #d6d6d6;border-radius:3px;margin:12px 4px 0;font-size:9px;color:#555;padding:0 8px;display:flex;align-items:center;justify-content:space-between}
.field.tall{height:64px;align-items:flex-start;padding-top:8px}
.submit{margin:14px 4px 0;height:42px;background:var(--plum-dark);color:var(--white);font-size:17px;font-weight:700;text-align:center;line-height:42px;border-radius:3px}

/* footer */
.footer{left:0;top:2378px;width:1200px;height:265px;background:linear-gradient(180deg,#2a2a2a,#1c1c1c)}
.foot-title{color:var(--magenta-bright);font-size:12px;font-weight:700;text-transform:uppercase}
.foot-text{color:#aaa;font-size:9px;line-height:15px}
.news-input{width:270px;height:26px;background:#555;color:#ddd;font-size:9px;padding:6px 8px}
.news-btn{width:94px;height:26px;background:var(--magenta);color:var(--white);font-size:10px;font-weight:700;text-align:center;line-height:26px;border-radius:3px}
.copyright{left:0;top:2643px;width:1200px;height:34px;background:#111;color:#888;font-size:9px;padding:12px 0 0 160px}
.social{left:850px;top:2648px;display:flex;gap:10px}
.social span{width:24px;height:24px;border-radius:50%}
</style>
</head>
<body>

<div class="abs hero-photo" role="img" aria-label="Photo of a technician giving a client a laser skin treatment, both wearing protective eyewear"></div>
<div class="abs hero-shade"></div>
<div class="abs topbar"></div>
<ul class="abs nav nav-left"><li>Home</li><li>About Us</li><li>Skin Renewal</li><li>Scar Removal</li></ul>
<ul class="abs nav nav-right"><li>Wart Removal</li><li>Your Visit</li><li>Contact Us</li><li>Blog</li></ul>
<div class="abs brand"><span class="brand-dot"></span><span class="brand-name">Maple Crest Glow Skin Studio</span></div>
<h1 class="abs hero-title">Make a start on the new you</h1>
<div class="abs call-pill"><small>Book your FREE consultation today</small><a href="tel:5550142280">(555) 014-2280</a></div>

<section class="abs offers">
  <h2>Restore your youthful skin this year!</h2>
  <p>Take advantage of our laser skin renewal specials for single or multiple sessions at low pricing.<br>Special ENDS January 3, 2015 at 5:00 PM.</p>
  <div class="deal" style="left:233px"><b>$199</b><span>1 Single<br>Session Deal</span></div>
  <svg class="deal-chev" style="left:430px" width="40" height="110" viewBox="0 0 40 110"><path d="M2 2 L38 55 L2 108" fill="none" stroke="#c64cc3" stroke-width="3"/></svg>
  <div class="deal" style="left:530px"><b>$549</b><span>3 Sessions<br>Package Deal</span></div>
  <svg class="deal-chev" style="left:730px" width="40" height="110" viewBox="0 0 40 110"><path d="M2 2 L38 55 L2 108" fill="none" stroke="#c64cc3" stroke-width="3"/></svg>
  <div class="deal" style="left:831px"><b>$899</b><span>6 Sessions<br>Package Deal</span></div>
</section>

<section class="abs intro-copy">
  <h2>Laser Skin Renewal is Innovative and Unique</h2>
  <p>Laser skin therapy is a non-invasive procedure that is extremely safe and effective. Above all, it is discrete and you never have to worry about family, friends and acquaintances, finding out that you have had treatment for fine lines and wrinkles.</p>
  <p>After each treatment, you will notice subtle but definite results. You will never have to hide indoors to wait for the skin irritation or bruising to disappear. The treatment sessions are comfortable and there is no worry about using topical anesthetic gels.</p>
  <p>Laser skin renewal does produce outstanding results. After mere five treatment sessions, you will notice a youthful glow about your skin and you also will find your skin looking smooth with an even tone. People, who have undergone laser treatment, also find their</p>
  <span class="btn-more">Read More</span>
</section>

<section class="abs faq">
  <div class="faq-item"><span class="faq-ico">&minus;</span>Have you considered Laser Skin Renewal Therapy?</div>
  <div class="faq-body">
    <p>You will truly love laser skin renewal if your skin is showing signs of premature aging or the skin has sustained sun damage. Conditions such as excessive redness due to sun exposure or fine lines will be concerns of the past.</p>
    <p>In fact, laser skin therapy is a unique and innovative way to enjoy youthful and healthy skin without resorting to painful and inconvenient surgery. Both men and women are receiving benefits from laser skin therapy.</p>
  </div>
  <div class="faq-item"><span class="faq-ico">+</span>How Does Laser Skin Renewal-Therapy Work?</div>
  <div class="faq-item"><span class="faq-ico">+</span>Are there any Side Effects of Laser Skin Renewal Therapy?</div>
</section>

<section class="abs benefits">
  <h2>Benefits Of Laser</h2>
  <div class="lead">Lorem ipsum dolor sit amet, consectetur adipiscing elit</div>
  <article class="card" style="left:160px">
    <div class="card-img" role="img" aria-label="Photo of a client receiving a facial skin treatment" style="background:linear-gradient(135deg,#f3d9c4,#d9a98a)"></div>
    <h3>Laser Skin Renewal Treatment</h3>
    <p>Laser skin renewal treatment could be just what you need to maintain your youthful appearance and get soft, smooth and evenly toned skin.</p>
    <span class="card-plus">+</span>
  </article>
  <article class="card" style="left:462px">
    <div class="card-img" role="img" aria-label="Photo of a gloved hand treating a wart on a foot" style="background:linear-gradient(135deg,#c9b6a6,#8e7667)"></div>
    <h3>Laser Wart Removal Treatment</h3>
    <p>Laser skin renewal treatment could be just what you need to maintain your youthful appearance and get soft, smooth and evenly toned skin.</p>
    <span class="card-plus">+</span>
  </article>
  <article class="card" style="left:761px">
    <div class="card-img" role="img" aria-label="Close-up photo of a laser pen treating a scar on skin" style="background:linear-gradient(135deg,#d9917f,#a8574a)"></div>
    <h3>Laser Scar Removal Treatment</h3>
    <p>Laser skin renewal treatment could be just what you need to maintain your youthful appearance and get soft, smooth and evenly toned skin.</p>
    <span class="card-plus">+</span>
  </article>
</section>

<section class="abs videos-head">
  <h2>Our Videos</h2>
  <p>Lorem ipsum dolor sit amet, consectetur adipiscing elit, sed do eiusmod tempor incididunt ut labore et dolore magna aliqua. Ut enim ad minim veniam, quis nostrud exercitation ullamco laboris nisi ut aliquip ex ea commodo consequat. Duis aute irure dolor in reprehenderit in voluptate velit esse cillum dolore eu fugiat nulla pariatur. Excepteur sint occaecat cupidatat non proident.</p>
</section>
<div class="abs video" role="img" aria-label="Video still of a clinician performing a laser skin treatment"></div>
<div class="abs video-btn"><svg width="12" height="14" viewBox="0 0 12 14"><path d="M0 0 L12 7 L0 14Z" fill="#fff"/></svg>Watch the Video</div>

<form class="abs consult">
  <h3>Request a Consultation</h3>
  <div class="field">Name</div>
  <div class="field">Email</div>
  <div class="field">Phone</div>
  <div class="field">Select Location <svg width="8" height="6" viewBox="0 0 8 6"><path d="M0 0 L8 0 L4 6Z" fill="#666"/></svg></div>
  <div class="field">Select Treatment <svg width="8" height="6" viewBox="0 0 8 6"><path d="M0 0 L8 0 L4 6Z" fill="#666"/></svg></div>
  <div class="field tall">Message</div>
  <div class="submit">SUBMIT</div>
</form>

<footer class="abs footer">
  <div class="abs foot-title" style="left:160px;top:26px">Join our news letter!</div>
  <div class="abs news-input" style="left:324px;top:20px">Enter Your Email</div>
  <div class="abs news-btn" style="left:608px;top:20px">SUBSCRIBE</div>

  <div class="abs foot-title" style="left:160px;top:76px">Quick Link</div>
  <div class="abs foot-text" style="left:160px;top:98px">Home<br>About Us<br>Skin Renewal<br>Scar Removal<br>Wart Removal</div>
  <div class="abs foot-text" style="left:316px;top:98px">Your Visit<br>Contact Us<br>Blog<br>Privacy Policy<br>Term of Conditions</div>

  <div class="abs foot-title" style="left:518px;top:76px">Contact Us</div>
  <div class="abs foot-text" style="left:518px;top:98px">MAPLE CREST GLOW SKIN STUDIO<br>Birchwood Wellness Plaza<br>480 Orchard Lane, Suite 12<br>Maple Crest, TX 70000<br><br>Tel : (555) 014-2280<br>Email : info@maplecrestglowskinstudio.example</div>

  <div class="abs foot-title" style="left:858px;top:26px">Recent Blog Post</div>
  <div class="abs foot-text" style="left:858px;top:52px;width:190px"><i>29 July, 2014</i><br>Sed ut perspiciatis unde omnis iste natus error sit voluptatem accusantium</div>
  <div class="abs foot-text" style="left:858px;top:118px;width:190px"><i>30 July, 2014</i><br>Nemo enim ipsam voluptatem quia voluptas sit aspernatur aut odit aut fugit</div>
  <div class="abs foot-text" style="left:858px;top:184px;width:190px"><i>31 August, 2014</i><br>At vero eos et accusamus et iusto odio dignissimos ducimus qui blanditiis</div>
</footer>
<div class="abs copyright">Copyright &copy; 2015 maplecrestglowskinstudio.example. All Rights Reserved.</div>
<div class="abs social" aria-label="Social links">
  <span style="background:#3aa4e6"></span><span style="background:#3b5b9a"></span><span style="background:#2f6eb5"></span><span style="background:#d23a3a"></span><span style="background:#1a77b5"></span><span style="background:#d8483a"></span>
</div>

</body>
</html>
```